Makeup Artist needs flyers to present his service package

I need a flyer to apply for my newly founded startup. I am an independent partner of the young brand Glamour Quest. Both my name "Miriam Kellbrand" and the attached logo should be represented, with the name in the foreground. The design should be clear and bright. The focus is on the professionalism of Miriam Kellbrand. The following topics / categories should be included in the flyer: 1.) Presentation of the person 2.) Skills Update (for the professional line) 3.) Style Update (for the private customer) 4.) Contact Text suggestions are attached as a file.

Target Market(s)

TV productions, high-priced private customers

Colors
9d9d9d
ffffff
474747

Requirements
Should not have
• No flowers, nothing playful. Not romantic.

```html
<!DOCTYPE html>
<html lang="de">
<head>
<meta charset="utf-8">
<title>Glamour Quest – Makeup by Miriam Kellbrand</title>
<link rel="stylesheet" href="https://fonts.googleapis.com/css2?family=Lato:wght@300;400;700;900&family=Montserrat:wght@300;700&display=swap">
<style>
:root{
  --grey-light:#9d9d9d;
  --white:#ffffff;
  --grey-dark:#474747;
  --ink:#2b2b2b;
  --band:#3a3a3a;
  --stage:#ececec;
}
*{box-sizing:border-box;margin:0;padding:0}
html,body{width:800px;height:1200px;overflow:hidden}
body{background:var(--stage);position:relative;font-family:'Lato',sans-serif}
.sheet{position:absolute;top:350px;width:385px;height:500px;background:var(--white);overflow:hidden;box-shadow:0 6px 18px rgba(0,0,0,.25)}
.sheet--front{left:10px}
.sheet--back{left:405px}

/* front */
.portrait{position:absolute;inset:0;background:linear-gradient(160deg,#8a8a8a 0%,#6a6a6a 40%,#4a4a4a 70%,#2a2a2a 100%)}
.front-shade{position:absolute;left:0;right:0;bottom:0;height:190px;background:linear-gradient(to bottom,rgba(0,0,0,0),rgba(0,0,0,.85))}
.brand{position:absolute;left:20px;top:22px;display:flex;align-items:center;gap:8px;color:var(--white);font-family:'Lato',sans-serif;font-weight:700;font-size:13px;letter-spacing:3px}
.brand-dot{width:16px;height:16px;border-radius:50%;background:var(--white)}
.title-by{position:absolute;left:0;top:322px;width:220px;height:32px;background:var(--band);color:var(--white);font-family:'Montserrat',sans-serif;font-weight:700;font-size:24px;line-height:32px;padding-left:18px}
.title-name{position:absolute;left:0;top:355px;width:216px;height:74px;background:var(--white);color:var(--grey-dark);font-family:'Montserrat',sans-serif;font-weight:300;font-size:29px;line-height:32px;padding:6px 0 0 18px}
.front-tagline{position:absolute;left:18px;top:442px;width:355px;color:var(--white);font-weight:700;font-size:7.6px;line-height:10px}
.front-url{position:absolute;left:18px;top:479px;right:0;display:flex;align-items:center;gap:6px;color:var(--white);font-weight:700;font-size:8px}
.front-url::after{content:"";flex:1;height:1px;background:var(--white)}

/* back */
.hero-photo{position:absolute;left:0;top:0;width:385px;height:115px;background:linear-gradient(180deg,#bdbdbd 0%,#7a7a7a 55%,#3e3e3e 100%)}
.tab{position:absolute;height:11px;background:var(--grey-light);color:var(--white);font-weight:700;font-size:7px;line-height:11px;padding-left:6px}
.tab--me{left:0;top:122px;width:55px}
.tab--skills{left:13px;top:232px;width:100px}
.tab--style{left:197px;top:232px;width:100px}
.copy{position:absolute;color:var(--grey-dark);font-size:5px;line-height:6.1px;text-align:justify}
.copy p+p{margin-top:3px}
.copy h3{font-size:6px;font-weight:700;color:var(--ink);margin-bottom:4px;text-align:left}
.copy--me{left:13px;top:137px;width:252px}
.mirror-photo{position:absolute;left:275px;top:122px;width:97px;height:102px;background:linear-gradient(135deg,#d8d8d8,#8c8c8c 60%,#4d4d4d)}
.copy--skills{left:13px;top:249px;width:165px}
.copy--style{left:197px;top:249px;width:175px}
.bullets{list-style:none;margin:0 0 5px 0}
.bullets li{position:relative;padding-left:9px;line-height:8.2px;text-align:left}
.bullets li::before{content:"";position:absolute;left:1px;top:2.2px;width:3.6px;height:3.6px;border-radius:50%;background:var(--grey-dark)}
.copy h3.sub{margin-top:6px}
.contact{position:absolute;left:0;bottom:0;width:200px;height:36px}
.contact svg{position:absolute;inset:0}
.contact-text{position:absolute;left:13px;top:4px;color:var(--white);font-size:5.2px;line-height:6.6px}
.contact-text .icon{display:inline-block;width:5px;height:5px;border-radius:50%;background:var(--white);vertical-align:-0.6px;margin-right:2px}
.contact-text .gap{margin-left:6px}
.foot-band{position:absolute;right:0;bottom:0;width:190px;height:18px}
.signoff{position:absolute;left:197px;top:446px;font-size:6px;color:var(--grey-dark)}
</style>
</head>
<body>

<section class="sheet sheet--front">
  <div class="portrait" role="img" aria-label="Black and white portrait of the makeup artist wearing dark glasses"></div>
  <div class="front-shade"></div>
  <div class="brand"><span class="brand-dot"></span>GLAMOUR QUEST</div>
  <h1 class="title-by">MAKEUP-BY</h1>
  <h2 class="title-name">MIRIAM<br>KELLBRAND</h2>
  <p class="front-tagline">Make-up &amp; Hairstyling in München, für TV, Foto, Event Veranstaltung, Business Make-up, Weiterbildung, Brautstyling, Make-up Coaching &amp; Workshops</p>
  <p class="front-url">www.glamour-quest.de/muenchen</p>
</section>

<section class="sheet sheet--back">
  <div class="hero-photo" role="img" aria-label="Makeup palette and brushes on a dressing table"></div>

  <div class="tab tab--me">ME</div>
  <div class="copy copy--me">
    <p>Seit vielen Jahren arbeite ich mit großer Leidenschaft für bekannte TV-, Foto-, und Showformate als Makeup Artist und Hairstylistin. Lena Hartwig und Carla Benning habe ich für Projekte im In- und Ausland begleitet, um mit ihnen an traumhaften Plätzen zu drehen. Bei verschiedenen Produktionen habe ich auch mit nationalen und internationalen Schauspielern sowie mit prominenten Politikern gearbeitet. Moderatoren und Celebrities vertrauen meiner fachlichen Kompetenz und schätzen meine Integrität.</p>
    <p>Nun habe ich mir auch noch einen Traum mit meinem Atelier in München erfüllt. Hier kann ich nun endlich jeden Beauty-Interessierten, ob Frau oder Mann, mit meinem Wissen und meiner Dienstleistung zur Seite stehen. Ob für ein Event oder eine Businessveranstaltung, dem Roten Teppich oder dem Brautstyling am schönsten Tag des Lebens.</p>
  </div>
  <div class="mirror-photo" role="img" aria-label="Artist at a lit makeup mirror"></div>

  <div class="tab tab--skills">SKILLS UPDATE</div>
  <div class="copy copy--skills">
    <h3>Das ist meine professionelle Linie für:</h3>
    <ul class="bullets">
      <li>HDTV Produktionen</li>
      <li>Fotoshootings und Produktionen in der Greenbox</li>
      <li>Fernsehsender, Fotografen und Agenturen</li>
      <li>Events, Show- und Galaveranstaltungen</li>
      <li>Auftritte auf dem Roten Teppich</li>
    </ul>
    <p>Um den Anforderungen von HD und 4K gerecht werden zu können, arbeite ich ausschließlich mit professionellen Ultra-HD Makeup Produkten. Bei Fotoshootings und Events verwende ich ebenfalls nur qualitativ hochwertige Markenprodukte, um den höchsten Ansprüchen gerecht werden zu können und eine perfekte Leistung zu garantieren. Außerdem gebe ich mein Wissen weiter an Fachkundige aus dem Kosmetik- oder Friseurhandwerk.</p>
    <h3 class="sub">In speziellen Workshops für Profis werden:</h3>
    <ul class="bullets">
      <li>Die Techniken des HDTV Makeups</li>
      <li>Produktlehre</li>
      <li>Makeup für Greenbox</li>
      <li>Hairstyling</li>
      <li>Braut Makeup und Brautstyling</li>
    </ul>
  </div>

  <div class="tab tab--style">STYLE UPDATE</div>
  <div class="copy copy--style">
    <h3>Mein schönes Ich</h3>
    <p>Sie sind Unternehmerin oder Businessfrau, Sie stellen Projekte vor und haben Videokonferenzen. Mit Ihrer Kompetenz stehen Sie im Fokus. Haben Sie ein Bewerbungsgespräch auf das Sie fachlich perfekt vorbereitet sind, aber noch keinen Gedanken über Ihr Styling gemacht haben?</p>
    <p>Unterstreichen Sie Ihren Auftritt mit einem strahlenden, frischen und femininen Makeup. Ein Business Makeup soll unaufdringlich aber selbstbewusst den eigenen Typ in Szene setzen. Ein gepflegter Look, der Ihrer Kompetenz noch das „i-Tüpfelchen“ aufsetzt.</p>
    <p>Sie sind eingeladen und Sie wollen ganz besonders schön aussehen. Ich unterstütze Sie.</p>
    <p>Im individuellen Einzelcoaching oder auch in einem Makeup Workshop lernen Sie die geheimen Tricks und Produkte eines professionellen Makeup Artist kennen. Sehen Sie wie schön Sie wirklich sind. Bald werden Sie Ihr eigener Beauty Profi sein, für Privat und Business.</p>
    <p>Alle Workshops können auch von Unternehmen als Corporate Makeup oder Firmenevent gebucht werden. Wenn nicht in München dann woanders, auch das ist möglich.</p>
  </div>
  <p class="signoff">Ich freue mich auf Sie, Ihre Miriam Kellbrand</p>

  <div class="contact">
    <svg width="200" height="36" viewBox="0 0 200 36" aria-hidden="true"><polygon points="0,0 186,0 200,36 0,36" fill="#474747"/></svg>
    <div class="contact-text">
      SPRECHEN SIE MICH DIREKT AN, UNTER<br>
      miriamkellbrand@glamour-quest.de<br>
      <span class="icon"></span>089/40012345<span class="gap"></span><span class="icon"></span>0151/40098765
    </div>
  </div>
  <svg class="foot-band" viewBox="0 0 190 18" aria-hidden="true"><polygon points="0,0 190,0 190,18 6,18" fill="#474747"/></svg>
</section>

</body>
</html>
```